Australian Software Consultancy needs new Business Card Design

Design Business Card based on existing design artefacts (attached). We are open to all designs. As its a 2 sided design and we thought it might be quite striking to have one side with a black background and te other side with a white background.

Target Market(s)

Financial Services mainly.

Industry/Entity Type

Business

Contact Information for Business Card

Name :
Position :
Email :

Requirements
Must have
• Funky design using our existing assets

```html
<!DOCTYPE html>
<html lang="en">
<head>
<meta charset="utf-8">
<title>Bright Lane – Business Card</title>
<link rel="stylesheet" href="https://fonts.googleapis.com/css2?family=Source+Sans+3:wght@400;600;800&display=swap">
<style>
  :root {
    --canvas: #e9e7e4;
    --brand-red: #e8202a;
    --card-white: #ffffff;
    --card-black: #111111;
    --ink-dark: #1a1a1a;
    --ink-light: #ffffff;
    --decor-circle: rgba(232, 32, 42, 0.28);
  }
  * { box-sizing: border-box; margin: 0; padding: 0; }
  html, body {
    width: 1200px; height: 1024px; overflow: hidden;
    background: var(--canvas);
    font-family: "Source Sans 3", Arial, sans-serif;
  }
  .card {
    position: absolute; left: 232px;
    width: 736px; height: 420px;
    border-radius: 34px; overflow: hidden;
    box-shadow: 0 10px 28px rgba(0,0,0,0.18);
  }
  .card--front { top: 64px; background: var(--card-white); }
  .card--back { top: 540px; background: var(--card-black); }
  .card__shape { position: absolute; inset: 0; }

  .brand {
    position: absolute; left: 70px; top: 36px; width: 320px;
    display: flex; flex-direction: column; align-items: center; gap: 12px;
  }
  .brand__dot {
    width: 60px; height: 60px; border-radius: 50%;
    border: 5px solid var(--brand-red);
  }
  .brand__name {
    font-weight: 800; font-size: 36px; letter-spacing: 1px; line-height: 1;
    color: var(--ink-dark); text-transform: uppercase;
  }

  .person {
    position: absolute; left: 44px; bottom: 26px;
    color: var(--ink-light); font-size: 18px; line-height: 1.3;
  }
  .person__name { font-weight: 600; font-size: 21px; }
  .person__role { margin-bottom: 10px; }

  .contact {
    position: absolute; right: 44px; top: 232px;
    list-style: none; color: var(--ink-light); font-size: 18px;
  }
  .contact__item { display: flex; align-items: center; gap: 10px; margin-bottom: 8px; }
  .contact__icon { width: 18px; height: 18px; flex: none; }

  .back-circle {
    position: absolute; left: 238px; top: 50px;
    width: 320px; height: 320px; border-radius: 50%;
    border: 22px solid var(--decor-circle);
  }
  .back-name {
    position: absolute; left: 0; right: 0; top: 160px;
    text-align: center; color: var(--ink-light);
    font-weight: 800; font-size: 72px; letter-spacing: 2px;
    text-transform: uppercase;
  }
  .back-web {
    position: absolute; left: 0; right: 0; top: 260px;
    text-align: center; color: var(--ink-light); font-size: 18px;
  }
</style>
</head>
<body>

<section class="card card--front">
  <svg class="card__shape" viewBox="0 0 736 420" aria-hidden="true">
    <path d="M0,262 Q470,262 736,20 L736,420 L0,420 Z" fill="var(--brand-red)"/>
    <path d="M0,280 Q480,280 736,40" fill="none" stroke="var(--card-white)" stroke-width="3"/>
  </svg>

  <div class="brand">
    <span class="brand__dot"></span>
    <span class="brand__name">Bright Lane</span>
  </div>

  <div class="person">
    <p class="person__name">Jordan Vale</p>
    <p class="person__role">Job Title</p>
    <p>120 Harbour Lane</p>
    <p>Seaview, California 90000</p>
  </div>

  <ul class="contact">
    <li class="contact__item">
      <svg class="contact__icon" viewBox="0 0 24 24"><path fill="#fff" d="M6.6 10.8a15 15 0 0 0 6.6 6.6l2.2-2.2a1 1 0 0 1 1-.25 11 11 0 0 0 3.6.57 1 1 0 0 1 1 1V20a1 1 0 0 1-1 1A17 17 0 0 1 3 4a1 1 0 0 1 1-1h3.5a1 1 0 0 1 1 1 11 11 0 0 0 .57 3.6 1 1 0 0 1-.25 1z"/></svg>
      555-010-2746
    </li>
    <li class="contact__item">
      <svg class="contact__icon" viewBox="0 0 24 24"><rect x="2" y="5" width="20" height="14" rx="1.5" fill="none" stroke="#fff" stroke-width="2"/><path d="M3 6l9 7 9-7" fill="none" stroke="#fff" stroke-width="2"/></svg>
      hello@sampledomain.com
    </li>
    <li class="contact__item">
      <svg class="contact__icon" viewBox="0 0 24 24"><circle cx="12" cy="12" r="9.5" fill="none" stroke="#fff" stroke-width="2"/><ellipse cx="12" cy="12" rx="4" ry="9.5" fill="none" stroke="#fff" stroke-width="1.6"/><path d="M2.5 12h19" stroke="#fff" stroke-width="1.6"/></svg>
      www.brightlane.com
    </li>
  </ul>
</section>

<section class="card card--back">
  <span class="back-circle" aria-hidden="true"></span>
  <h1 class="back-name">Bright Lane</h1>
  <p class="back-web">www.brightlane.com</p>
</section>

</body>
</html>
```